Just Sold Postcard

Real Estate/ Bramwell Oakes Realty.I'd like a template that I can use to change out the picture of the home, verbiage on the front, and address. I'm including a picture of what I've used in the past. I like designs that use red, with some blue and white. I'd like the ability to change the verbiage on the back as well.

Industry/Entity Type

Real Estate

Font styles to use
Serif
Sans Serif

```html
<!DOCTYPE html>
<html lang="en">
<head>
<meta charset="utf-8">
<title>Just Sold Postcard – Bramwell Oakes Realty</title>
<link href="https://fonts.googleapis.com/css2?family=Anton&family=Cinzel:wght@500;600&family=Roboto:wght@500;700;900&display=swap" rel="stylesheet">
<style>
  :root{
    --bg:#ece8e3;
    --red-dark:#7a1414;
    --red:#b3201f;
    --red-bright:#d62a1e;
    --navy:#1f2f7a;
    --navy-dark:#172466;
    --blue:#1d4a9a;
    --yellow:#ffe21a;
    --white:#ffffff;
    --ink:#222;
    --rule:#333;
  }
  *{margin:0;padding:0;box-sizing:border-box}
  html,body{width:907px;height:1200px;overflow:hidden;background:var(--bg)}
  body{position:relative;font-family:"Roboto",Arial,sans-serif}

  .postcard{position:absolute;left:138px;width:645px;height:500px;background:var(--white);
    box-shadow:0 4px 12px rgba(0,0,0,.25);overflow:hidden}
  .postcard--front{top:48px}
  .postcard--back{top:645px}

  .layer{position:absolute;left:0;top:0}

  /* front */
  .listing-address{position:absolute;left:26px;top:32px;font-weight:900;font-size:25px;color:var(--yellow);letter-spacing:.3px}
  .listing-details{position:absolute;left:28px;top:70px;font-family:"Cinzel",Georgia,serif;font-weight:600;font-size:16.5px;line-height:22px;color:var(--white);letter-spacing:.4px}
  .sold-headline{position:absolute;left:20px;top:150px;font-family:"Anton",Impact,sans-serif;font-size:64px;line-height:1;color:var(--yellow);
    transform:rotate(-4deg) skewX(-4deg);transform-origin:left top;text-shadow:2px 3px 0 rgba(90,0,0,.55)}
  .sold-banner{position:absolute;left:34px;top:236px;width:246px;height:50px;background:var(--navy);
    transform:rotate(-4deg);transform-origin:left top;display:flex;align-items:center;justify-content:center;
    font-family:"Roboto",Arial,sans-serif;font-weight:900;font-size:31px;color:var(--white);box-shadow:0 3px 4px rgba(0,0,0,.3)}
  .agent-name{position:absolute;left:22px;top:397px;font-weight:700;font-size:27px;color:var(--red)}
  .agent-tagline{position:absolute;left:24px;top:433px;font-family:"Cinzel",Georgia,serif;font-weight:600;font-size:15px;color:var(--ink)}
  .agent-phone{position:absolute;left:24px;top:456px;font-weight:700;font-size:20px;color:var(--navy)}
  .brand{position:absolute;display:flex;align-items:center;gap:8px;font-family:"Roboto",Arial,sans-serif;font-weight:700;color:var(--red)}
  .brand__mark{width:14px;height:14px;background:var(--navy);flex:none}
  .postcard--front .brand{left:372px;top:420px;font-size:23px}

  /* back */
  .back-panel{position:absolute;left:0;top:0;width:312px;height:500px}
  .postcard--back .brand{left:0;width:312px;justify-content:center;top:40px;font-size:20px}
  .panel-text{position:absolute;left:0;width:312px;text-align:center}
  .panel-address{top:284px;font-family:"Cinzel",Georgia,serif;font-weight:500;font-size:11px;color:var(--white);letter-spacing:.5px}
  .panel-name{top:325px;font-weight:900;font-size:16px;color:var(--yellow);letter-spacing:.3px}
  .panel-phone{top:345px;font-weight:700;font-size:20px;color:var(--white)}
  .panel-cta{top:378px;font-weight:700;font-size:14.5px;color:var(--yellow)}
  .panel-offer{top:397px;font-family:"Cinzel",Georgia,serif;font-weight:600;font-size:12.5px;line-height:17px;color:var(--white)}
  .contact-row{position:absolute;left:62px;display:flex;align-items:center;gap:9px;color:var(--white)}
  .contact-row--phone{top:446px;font-weight:700;font-size:19px}
  .contact-row--email{top:473px;font-weight:500;font-size:13.5px}
  .contact-icon{width:17px;height:15px;background:var(--yellow);border-radius:3px;display:flex;align-items:center;justify-content:center}

  .mail-side{position:absolute;left:312px;top:0;width:333px;height:500px;font-family:Arial,Helvetica,sans-serif;color:#111}
  .postage-box{position:absolute;left:173px;top:18px;width:142px;height:142px;border:1.5px solid var(--rule);
    display:flex;justify-content:center;padding-top:52px;text-align:center;font-size:15px;line-height:20px}
  .mail-label{position:absolute;left:34px;top:198px;font-size:16px}
  .mail-line{position:absolute;left:34px;width:264px;border-top:1.3px solid var(--rule)}
</style>
</head>
<body>

<section class="postcard postcard--front" aria-label="Postcard front">
  <svg class="layer" width="645" height="500" viewBox="0 0 645 500" aria-hidden="true">
    <defs>
      <linearGradient id="redBand" x1="0" y1="0" x2="0" y2="1">
        <stop offset="0" stop-color="#6e1010"/><stop offset=".55" stop-color="#a01c1a"/><stop offset="1" stop-color="#d3281c"/>
      </linearGradient>
    </defs>
    <rect width="645" height="500" fill="#f2f2f2"/>
    <path d="M0 0H645V118C560 108 470 150 390 185 290 230 160 240 0 255Z" fill="url(#redBand)"/>
  </svg>
  <svg class="layer" width="645" height="500" viewBox="0 0 645 500" role="img" aria-label="Photo of the sold home: two-storey craftsman house with gables and landscaped front garden">
    <defs>
      <linearGradient id="frontPhoto" x1="0" y1="0" x2="0" y2="1">
        <stop offset="0" stop-color="#4d86c8"/><stop offset=".35" stop-color="#8b8474"/><stop offset=".7" stop-color="#4f6b35"/><stop offset="1" stop-color="#2f4a22"/>
      </linearGradient>
    </defs>
    <path d="M645 124C560 114 470 156 390 191 290 236 160 246 0 261V300C90 350 200 400 310 405 430 410 540 370 645 372Z" fill="url(#frontPhoto)"/>
  </svg>
  <svg class="layer" width="645" height="500" viewBox="0 0 645 500" aria-hidden="true">
    <path d="M645 116C560 106 470 148 390 183 290 228 160 238 0 253" fill="none" stroke="#fff" stroke-width="7"/>
    <path d="M0 300C90 350 200 400 310 405 430 410 540 370 645 372" fill="none" stroke="var(--navy)" stroke-width="4"/>
    <path d="M0 306C90 356 200 406 310 411 430 416 540 376 645 378V384C540 382 430 420 310 417 200 412 90 362 0 314Z" fill="#c8c8c8"/>
  </svg>

  <h2 class="listing-address">1172 JUNIPER RIDGE DRIVE</h2>
  <p class="listing-details">Fabulous End Unit with granite<br>contertops and &nbsp;hardwood floors.<br>Private lot</p>
  <h1 class="sold-headline">Just Sold!</h1>
  <div class="sold-banner">Brought Buyer</div>

  <p class="agent-name">Dana Whitfield</p>
  <p class="agent-tagline">Your Neighborhood Expert</p>
  <p class="agent-phone">555.214.0389</p>
  <div class="brand"><span class="brand__mark"></span>Bramwell Oakes Realty</div>
</section>

<section class="postcard postcard--back" aria-label="Postcard back">
  <div class="back-panel">
    <svg class="layer" width="312" height="500" viewBox="0 0 312 500" aria-hidden="true">
      <defs>
        <linearGradient id="skyTop" x1="0" y1="0" x2="0" y2="1">
          <stop offset="0" stop-color="#ffffff"/><stop offset="1" stop-color="#c9d9ee"/>
        </linearGradient>
        <linearGradient id="bluePanel" x1="0" y1="0" x2="0" y2="1">
          <stop offset="0" stop-color="#1d4fa0"/><stop offset="1" stop-color="#222f80"/>
        </linearGradient>
      </defs>
      <rect width="312" height="100" fill="url(#skyTop)"/>
      <path d="M0 262C90 252 200 256 312 268V500H0Z" fill="url(#bluePanel)"/>
    </svg>
    <svg class="layer" width="312" height="500" viewBox="0 0 312 500" role="img" aria-label="Photo of a two-storey family home with a double garage and front lawn">
      <defs>
        <linearGradient id="backPhoto" x1="0" y1="0" x2="0" y2="1">
          <stop offset="0" stop-color="#b7cce6"/><stop offset=".45" stop-color="#6f6e62"/><stop offset=".8" stop-color="#5e7f3f"/><stop offset="1" stop-color="#9aa39a"/>
        </linearGradient>
      </defs>
      <path d="M0 100H312V250C200 240 90 244 0 256Z" fill="url(#backPhoto)"/>
    </svg>
    <svg class="layer" width="312" height="500" viewBox="0 0 312 500" aria-hidden="true">
      <path d="M0 256C90 244 200 240 312 250V268C200 256 90 252 0 262Z" fill="#e9e9e9"/>
      <path d="M0 262C90 252 200 256 312 268" fill="none" stroke="#9a9a9a" stroke-width="1.5"/>
    </svg>

    <div class="brand"><span class="brand__mark"></span>Bramwell Oakes Realty</div>
    <p class="panel-text panel-address">Address</p>
    <p class="panel-text panel-name">DANA WHITFIELD</p>
    <p class="panel-text panel-phone">555.214.0389</p>
    <p class="panel-text panel-cta">Contact Me Today!</p>
    <p class="panel-text panel-offer">For a free Market<br>Analysis of your home!</p>
    <div class="contact-row contact-row--phone">
      <span class="contact-icon"><svg width="11" height="11" viewBox="0 0 24 24" aria-hidden="true"><path d="M6.6 10.8a15 15 0 0 0 6.6 6.6l2.2-2.2c.3-.3.7-.4 1-.2 1.1.4 2.3.6 3.6.6.6 0 1 .4 1 1V20c0 .6-.4 1-1 1A17 17 0 0 1 3 4c0-.6.4-1 1-1h3.5c.6 0 1 .4 1 1 0 1.3.2 2.5.6 3.6.1.3 0 .7-.2 1z" fill="var(--navy-dark)"/></svg></span>
      555.214.0389
    </div>
    <div class="contact-row contact-row--email">
      <span class="contact-icon"><svg width="11" height="9" viewBox="0 0 22 16" aria-hidden="true"><rect x="1" y="1" width="20" height="14" fill="none" stroke="var(--navy-dark)" stroke-width="2"/><path d="M1 1l10 8 10-8" fill="none" stroke="var(--navy-dark)" stroke-width="2"/></svg></span>
      dana.whitfield@example.com
    </div>
  </div>

  <div class="mail-side">
    <div class="postage-box">Postage<br>Area</div>
    <p class="mail-label">Address</p>
    <span class="mail-line" style="top:259px"></span>
    <span class="mail-line" style="top:305px"></span>
    <span class="mail-line" style="top:351px"></span>
    <span class="mail-line" style="top:397px"></span>
  </div>
</section>

</body>
</html>
```